Yoga class opening. Little schedule for JUNE JULY and AUGUST

Flyer to promote an opening yoga class. The color of the docx haven't to be respected.

We want something joyfull, professional, clean and serious.

About the logo we oppened a contest at the same time so at the moment there is no logo but the logo color will be simple.

The phone number will change so you can poste a random one for the design that i can change by myself.

i recieved many creation in both side BUT i want something in 1 side :)

Target Market(s)

Yoga student. all age

Industry/Entity Type

It Professional

Logo Text

Yoga fern

Font styles to use
Sans Serif

Requirements
Must have
• The text present on the docx
Nice to have
• Some symbols about yoga ( Namasté signs, mandala, ... )
Should not have
• Not too much details it has to be clear.

```html
<!DOCTYPE html>
<html lang="fr">
<head>
<meta charset="utf-8">
<title>Yoga Fern – Flyer d'ouverture</title>
<link rel="stylesheet" href="https://fonts.googleapis.com/css2?family=Oswald:wght@400;600;700&family=Ubuntu:wght@300;400;500;700&family=Open+Sans:wght@300;400&display=swap">
<style>
  :root{
    --backdrop:#774c2b;
    --sky:#2fa5d8;
    --orange:#f5904f;
    --orange-deep:#e07a2c;
    --orange-title:#f08a4b;
    --ink:#2e2e2e;
    --white:#ffffff;
  }
  *{margin:0;padding:0;box-sizing:border-box}
  html,body{width:988px;height:1200px;overflow:hidden;background:var(--backdrop)}
  .flyer{position:absolute;left:104px;top:105px;width:782px;height:1008px;background:var(--sky);
    box-shadow:4px 6px 10px rgba(0,0,0,.45);overflow:hidden;font-family:"Ubuntu",sans-serif;color:var(--white)}
  .hero-photo{position:absolute;left:0;top:0;width:782px;height:508px;
    background:
      linear-gradient(180deg,rgba(255,255,255,0) 85%,rgba(170,120,90,.55) 100%),
      radial-gradient(ellipse at 78% 60%,#8a6a9a 0 8%,transparent 22%),
      linear-gradient(90deg,#fbfbf6 0%,#f6f3de 22%,#e4e29a 40%,#a8b84a 58%,#5f7f2c 78%,#3d5a22 100%)}
  .abs{position:absolute}
  .headline{font-family:"Oswald",sans-serif;font-weight:700;color:var(--ink);text-transform:uppercase;line-height:1}
  .headline--big{left:35px;top:30px;font-size:45px}
  .headline--sub{left:35px;top:84px;font-size:33px;line-height:43px}
  .brand{left:440px;top:22px;font-family:"Open Sans",sans-serif;font-weight:400;font-size:58px;letter-spacing:2px;color:var(--orange-title)}
  .opening{left:35px;top:207px;font-family:"Ubuntu",sans-serif;font-weight:500;font-size:27px;color:#111}
  .address{left:35px;top:250px;font-size:21px;line-height:26px;color:#111}
  .intro{left:35px;top:344px;font-size:19.5px;line-height:26px;color:#111;width:300px}
  .web-tab{left:48px;top:467px;width:360px;height:56px}
  .web-tab span{position:absolute;left:0;right:0;top:6px;text-align:center;font-family:"Oswald",sans-serif;font-weight:600;
    font-size:32px;letter-spacing:3px;color:var(--white)}
  .month{position:absolute;height:26px;background:var(--orange);box-shadow:2px 2px 3px rgba(0,0,0,.25);
    font-weight:700;font-size:19px;line-height:26px;padding-left:10px;text-transform:uppercase}
  .course{position:absolute;font-weight:500;font-size:14.5px;white-space:nowrap}
  .slots{position:absolute;font-size:11.3px;line-height:16.8px;white-space:nowrap;list-style:none;font-weight:300}
  .rule{position:absolute;height:1.5px;background:var(--white)}
  .kickoff{left:390px;width:380px;top:683px;text-align:center;font-family:"Oswald",sans-serif;font-weight:700;
    font-size:27px;line-height:38px;text-shadow:1px 2px 3px rgba(0,0,0,.35)}
  .info-box{left:414px;top:773px;width:328px;height:120px;background:var(--orange);border:3px solid var(--white);
    border-radius:14px;box-shadow:2px 3px 5px rgba(0,0,0,.3);text-align:center}
  .info-box .lead{margin-top:10px;font-weight:700;font-size:21px;color:#1b1b1b}
  .info-box .alt{margin-top:4px;font-family:"Oswald",sans-serif;font-weight:400;font-size:15.5px}
  .info-box .wish{margin-top:2px;font-family:"Open Sans",sans-serif;font-weight:300;font-size:27px;letter-spacing:1px}
  .contact{position:absolute;left:448px;display:flex;align-items:center;gap:14px}
  .contact--phone{top:916px}
  .contact--mail{top:959px}
  .contact .phone-number{font-family:"Oswald",sans-serif;font-weight:700;font-size:30px}
  .contact .mail-address{font-family:"Ubuntu",sans-serif;font-weight:500;font-size:22px;letter-spacing:.5px}
</style>
</head>
<body>
<main class="flyer">
  <div class="hero-photo" role="img" aria-label="Photo d'une femme en posture de yoga sur un tapis, dans un parc ensoleillé"></div>

  <h1 class="abs headline headline--big">Nouveau !!</h1>
  <h2 class="abs headline headline--sub">Votre studio de<br>yoga a Ixelles</h2>
  <div class="abs brand">YOGA FERN</div>

  <p class="abs opening">OUVERTURE LE 6 JUIN 2016 AU</p>
  <p class="abs address">212 RUE DES TILLEULS<br>1050 IXELLES</p>
  <p class="abs intro">En attendant le planning des cours de la rentrée, YOGA FERN vous propose ses stages et ateliers d’été.</p>

  <div class="abs web-tab">
    <svg width="360" height="56" viewBox="0 0 360 56">
      <path d="M0 50 L8 56 L14 50 Z" fill="#8a3d12"/>
      <path d="M346 50 L352 56 L360 50 Z" fill="#8a3d12"/>
      <path d="M0 50 L30 2 Q32 0 36 0 L324 0 Q328 0 330 2 L360 50 Z" fill="var(--orange-deep)"/>
    </svg>
    <span>www.YogaFern.com</span>
  </div>

  <!-- Juin -->
  <div class="month" style="left:24px;top:535px;width:344px">Juin</div>
  <div class="course" style="left:33px;top:566px">Stage découverte du YOGA 10h00 85 € :</div>
  <ul class="slots" style="left:33px;top:590px">
    <li>Du lundi 6 au vendredi 10 juin : 10h00 à 12h00 ou 18h00 à 20h00</li>
    <li>Du lundi 13 au vendredi 17 juin : 10h00 à 12h00 ou 18h00 à 20h00</li>
    <li>Du lundi 20 au vendredi 24 juin : 10h00 à 12h00 ou 18h00 à 20h00</li>
    <li>Du lundi 27 au vendredi 1er juillet : 10h00 à 12h00 ou 18h00 à 20h00</li>
  </ul>
  <div class="rule" style="left:31px;top:660px;width:340px"></div>
  <div class="course" style="left:33px;top:667px">Atelier gestion du stress yoga/sophrologie 2h00 28 €</div>
  <ul class="slots" style="left:33px;top:691px">
    <li>Samedi 11 juin 10h30 à 12h30</li>
    <li>Samedi 11 juin 15h à 17h00</li>
    <li>Dimanche 12 juin 10h30 à 12h30</li>
    <li>Dimanche 12 juin 14h à 16h00</li>
  </ul>

  <!-- Juillet -->
  <div class="month" style="left:24px;top:768px;width:344px">Juillet</div>
  <div class="course" style="left:33px;top:800px">Stage initiation à l’ASHTANGA 10h00 85 €</div>
  <ul class="slots" style="left:33px;top:824px">
    <li>Du lundi 4 au vendredi 8 juillet : 10h00 à 12h00 ou 18h00 à 20h00</li>
    <li>Du lundi 11 au vendredi 15 juillet : 10h00 à 12h00 ou 18h00 à 20h00</li>
    <li>Du lundi 18 au vendredi 22 juillet : 10h00 à 12h00 ou 18h00 à 20h00</li>
    <li>Du lundi 25 au vendredi 29 juillet : 10h00 à 12h00 ou 18h00 à 20h00</li>
  </ul>
  <div class="rule" style="left:31px;top:893px;width:340px"></div>
  <div class="course" style="left:33px;top:899px">Atelier gestion du stress yoga/sophrologie 2h00 28 €</div>
  <ul class="slots" style="left:33px;top:923px">
    <li>Samedi 9 juillet 10h30 à 12h30</li>
    <li>Samedi 9 juillet 15h00 à 17h00</li>
    <li>Dimanche 10 juillet 10h30 à 12h30</li>
    <li>Dimanche 10 juillet 14h00 à 16h00</li>
  </ul>

  <!-- Août -->
  <div class="month" style="left:405px;top:535px;width:345px">Aout</div>
  <div class="course" style="left:415px;top:571px">Stage découverte du YOGA 10h00 85 €</div>
  <ul class="slots" style="left:415px;top:595px">
    <li>Du lundi 1er au vendredi 5 août : 10h00 à 12h00 ou 18h00 à 20h00</li>
    <li>Du lundi 8 au vendredi 12 août: 10h00 à 12h00 ou 18h00 à 20h00</li>
    <li>Du lundi 15 au vendredi 19 août: 10h00 à 12h00 ou 18h00 à 20h00</li>
    <li>Du lundi 22 au vendredi 26août: 10h00 à 12h00 ou 18h00 à 20h00</li>
  </ul>

  <p class="abs kickoff">Démarrage du planning<br>annuel le 5 septembre 2016</p>

  <div class="abs info-box">
    <p class="lead">Plus d’info et inscription:</p>
    <p class="alt">Ou via notre page facebook : yoga fern</p>
    <p class="wish">UN BEL ETE A TOUS !</p>
  </div>

  <div class="contact contact--phone">
    <svg width="30" height="30" viewBox="0 0 30 30" aria-hidden="true">
      <circle cx="15" cy="15" r="13" fill="none" stroke="#fff" stroke-width="2"/>
      <path d="M11 8 Q8 9 9 13 Q11 19 16 22 Q20 23 22 20 L19 17 L17 18 Q14 16 13 13 L14 11 Z" fill="#fff"/>
    </svg>
    <span class="phone-number">+1 555-014-2290</span>
  </div>
  <div class="contact contact--mail">
    <svg width="34" height="26" viewBox="0 0 34 26" aria-hidden="true">
      <rect x="1" y="2" width="30" height="20" fill="#fff" stroke="#d6e6ee"/>
      <path d="M1 2 L16 14 L31 2" fill="none" stroke="#9ab7c6" stroke-width="1.5"/>
      <path d="M22 20 L32 20 M26 16 L22 20 L26 24" fill="none" stroke="#1d6fa0" stroke-width="2.2"/>
    </svg>
    <span class="mail-address">info@yogafern.com</span>
  </div>
</main>
</body>
</html>
```